Organic skincare label - minimalist, earthy, luxe design needed!

I need a label design for a luxury natural skin care line called "Velka Botanix". Velka means 'earth' in Swahili. I would like the design to embody an earthy feel but be minimalistic and give a luxe vibe. My first product will be a Tumeric and Neem Scrub.

The size of the jar is 8oz, label dimensions should be (1.625" Tall x 8.5" Wide)
I will be making other products too such as; oils + toners so I feel free to do labels for glass bottles and/or spray bottles as well.

Forest green, light pinks/nudes/beige, grey, white, gold, are colors that can be used (not all have to be used).

I have included pictures of some things I've worked on myself as well as my original logo design but I need to simplify the logo, no circle around it.
Feel free to get creative.

Thank you! :)
Updates

Target Market(s)

Socially Conscious, Beauty Enthusiast, Minimalist

Industry/Entity Type

Skin Care

Font styles to use
Sans Serif
Other font styles liked:
• "Wonderlove doodle" is the font used for "Velka" in the logo. Feel free to use that or change it as you see fit.

Requirements
Must have
• Simplistic design
would like to stick to a font close to the ones in the logo. Either the one used for the name "Velka" OR the one that the slogan "ROOTED RITUALS" uses.

I have also included some pictures to capture the aesthetic of my social media and website.

Gender neutral

```html
<!DOCTYPE html>
<html lang="en">
<head>
<meta charset="utf-8">
<title>Velka Botanix – Tumeric and Neem Scrub Label</title>
<link rel="stylesheet" href="https://fonts.googleapis.com/css2?family=Inter+Tight:wght@400;600;700;800&display=swap">
<style>
  :root {
    --page-bg: #f3f3f3;
    --label-pink: #cfa3b7;
    --label-pink-deep: #c297ab;
    --leaf-light: #c79cb0;
    --leaf-dark: #a87a90;
    --accent-magenta: #d6005f;
    --ink-white: #ffffff;
    --ink-soft: #f6eef2;
  }
  html, body {
    margin: 0;
    width: 1200px;
    height: 1200px;
    overflow: hidden;
    background: var(--page-bg);
  }
  .canvas {
    position: relative;
    width: 1200px;
    height: 1200px;
  }
  .label {
    position: absolute;
    left: 100px;
    top: 325px;
    width: 1000px;
    height: 550px;
    overflow: hidden;
  }
  .label svg { display: block; }
  .product-title {
    font-family: "Inter Tight", "Helvetica Neue", Arial, sans-serif;
    font-weight: 800;
    fill: var(--ink-white);
    letter-spacing: -5px;
  }
  .product-title--small { letter-spacing: -3px; }
  .brand-name {
    font-family: "Inter Tight", Arial, sans-serif;
    font-weight: 700;
    fill: var(--ink-white);
    letter-spacing: 1px;
  }
  .brand-tagline {
    font-family: "Inter Tight", Arial, sans-serif;
    font-weight: 600;
    fill: var(--ink-white);
    letter-spacing: 0.6px;
  }
  .net-weight {
    font-family: "Inter Tight", Arial, sans-serif;
    font-weight: 400;
    fill: var(--ink-white);
    letter-spacing: 2px;
  }
  .ingredients {
    font-family: "Inter Tight", Arial, sans-serif;
    font-weight: 400;
    fill: var(--ink-soft);
  }
  .origin {
    font-family: "Inter Tight", Arial, sans-serif;
    font-weight: 700;
    fill: var(--ink-white);
    letter-spacing: -0.2px;
  }
</style>
</head>
<body>
<main class="canvas">
  <section class="label" aria-label="Velka Botanix Tumeric and Neem Scrub label">
    <svg width="1000" height="550" viewBox="0 0 1000 550" xmlns="http://www.w3.org/2000/svg">
      <defs>
        <linearGradient id="label-ground" x1="0" y1="0" x2="1" y2="0">
          <stop offset="0" stop-color="var(--label-pink)"/>
          <stop offset="1" stop-color="var(--label-pink-deep)"/>
        </linearGradient>
        <linearGradient id="leaf-tone" x1="0" y1="0" x2="1" y2="1">
          <stop offset="0" stop-color="var(--leaf-light)"/>
          <stop offset="0.55" stop-color="#bd92a6"/>
          <stop offset="1" stop-color="var(--leaf-dark)"/>
        </linearGradient>
      </defs>

      <rect class="label-ground" x="0" y="0" width="1000" height="550" fill="url(#label-ground)"/>

      <rect class="leaf-photo" x="573" y="0" width="427" height="550" fill="url(#leaf-tone)"
            role="img" aria-label="Photograph of a dried palm leaf tinted dusty rose"/>

      <rect class="accent-bar" x="553" y="0" width="46" height="414" fill="var(--accent-magenta)"/>

      <text class="product-title" x="9" y="108" font-size="140">Tumeric</text>
      <text class="product-title product-title--small" x="22" y="209" font-size="104">and</text>
      <text class="product-title" x="8" y="386" font-size="175">Neem</text>
      <text class="product-title" x="4" y="562" font-size="170">Scrub</text>

      <g class="brand-lockup">
        <circle cx="785" cy="191" r="6" fill="var(--ink-white)"/>
        <text class="brand-name" x="862" y="207" font-size="46" text-anchor="middle">Velka</text>
        <text class="brand-tagline" x="858" y="250" font-size="17" text-anchor="middle">ROOTED RITUALS</text>
      </g>

      <text class="net-weight" x="766" y="330" font-size="22">1.0 oz/28 g</text>

      <text class="ingredients" font-size="13">
        <tspan x="766" y="388">Ingredients: Organic Cane</tspan>
        <tspan x="766" y="406">Sugar, Organic Coconut oil,</tspan>
        <tspan x="766" y="424">Natural Coconut Flavoring</tspan>
      </text>

      <text class="origin" x="766" y="460" font-size="15">MADE IN HOUSTON, TX</text>
    </svg>
  </section>
</main>
</body>
</html>
```